Vowsbridge-Officiants.com Rack Card Design, Double-Sided. See Attachments.

Please use the attached graphics and the contents of www.vowsbridge-officiants.com to create a rack card that has the same look, feel and colors as the website, business card and existing logos. Your design must be consistent with how the business cards and website currently look.

Target Market(s)

weddings. Visit www.vowsbridge-officiants.com for content and design ideas.

Requirements
Must have
• Same info as business card plus content from the website.

```html
<!DOCTYPE html>
<html lang="en">
<head>
<meta charset="utf-8">
<title>Vowsbridge-Officiants.com Rack Card</title>
<link rel="stylesheet" href="https://fonts.googleapis.com/css2?family=Playfair+Display:wght@400;700;900&family=Raleway:wght@200;300&family=Inter:wght@400&family=Libre+Caslon+Text:wght@400;700&display=swap">
<style>
  :root {
    --backdrop: #cbcbcb;
    --taupe: #928a7c;
    --ink-light: #ffffff;
    --sky-bright: #e4e9ec;
    --sky-top: #b9c4cb;
    --sky-low: #8e9ba3;
    --hills: #4f5a5c;
    --meadow: #7a7548;
    --meadow-green: #6b7a3e;
    --path: #5e4a3b;
    --grove-dark: #1f2a18;
    --grove-mid: #3f5129;
    --grove-light: #8c9a62;
  }
  * { margin: 0; padding: 0; box-sizing: border-box; }
  html, body { width: 1200px; height: 961px; overflow: hidden; background: var(--backdrop); }
  .rack-card {
    position: absolute; left: 392px; top: 21px; width: 415px; height: 917px;
    background: var(--taupe); color: var(--ink-light);
    display: flex; flex-direction: column; text-align: center;
  }
  .photo-couple-meadow {
    height: 339px;
    background:
      radial-gradient(ellipse 60% 30% at 45% 5%, rgba(240,244,246,0.9) 0%, rgba(240,244,246,0) 100%),
      radial-gradient(ellipse 45% 35% at 38% 75%, rgba(120,96,74,0.7) 0%, rgba(120,96,74,0) 100%),
      linear-gradient(180deg, var(--sky-top) 0%, var(--sky-low) 34%, var(--hills) 46%, var(--meadow-green) 54%, var(--meadow) 72%, var(--path) 100%);
  }
  .intro-band { height: 207px; padding-top: 3px; }
  .headline {
    font-family: "Playfair Display", serif; font-weight: 900;
    font-size: 55px; line-height: 56px; letter-spacing: -0.5px;
  }
  .lead-in {
    font-family: "Raleway", sans-serif; font-weight: 200;
    font-size: 20px; line-height: 22px; margin-top: -3px;
  }
  .business-name {
    font-family: "Playfair Display", serif; font-weight: 700;
    font-size: 21px; line-height: 28px; margin-top: 1px;
  }
  .tagline {
    font-family: "Libre Caslon Text", serif; font-weight: 400;
    font-size: 18px; line-height: 24px;
    width: 113px; margin: 10px auto 0; border-top: 1px solid var(--ink-light); border-bottom: 1px solid var(--ink-light);
    padding: 3px 0 4px; white-space: nowrap;
    display: flex; justify-content: center;
  }
  .promise {
    font-family: "Inter", sans-serif; font-size: 10.5px; line-height: 15.5px;
    margin-top: 12px;
  }
  .photo-couple-grove {
    height: 221px;
    background:
      radial-gradient(ellipse 35% 40% at 48% 62%, rgba(196,204,170,0.55) 0%, rgba(196,204,170,0) 100%),
      linear-gradient(180deg, var(--grove-dark) 0%, var(--grove-mid) 35%, #55683a 60%, var(--grove-light) 82%, #5d6b3c 100%);
  }
  .contact-band {
    flex: 1; display: flex; flex-direction: column; align-items: center;
    padding-top: 20px;
  }
  .brand-name {
    font-family: "Libre Caslon Text", serif; font-weight: 400;
    font-size: 17px; line-height: 22px; display: flex; align-items: center; gap: 8px;
  }
  .brand-mark { width: 18px; height: 18px; border-radius: 50%; border: 1.5px solid var(--ink-light); }
  .contact-list {
    list-style: none; margin-top: 32px;
    font-family: "Libre Caslon Text", serif; font-weight: 700;
    font-size: 9.6px; line-height: 15.5px;
  }
</style>
</head>
<body>
  <main class="rack-card">
    <div class="photo-couple-meadow" role="img" aria-label="Bride and groom running barefoot hand in hand along a meadow path past a branch wedding arch, misty hills behind"></div>

    <section class="intro-band">
      <h1 class="headline">Your Wedding</h1>
      <p class="lead-in">starts here at</p>
      <p class="business-name">Marisol's Vowsbridge-Officiants.com</p>
      <p class="tagline">More Than Just a Marriage Officiant</p>
      <p class="promise">I'll work day and night to guarantee that your next event will<br>be filled with unforgettable moments.</p>
    </section>

    <div class="photo-couple-grove" role="img" aria-label="Newlyweds walking hand in hand through tall grass in a tree-lined orchard, seen from behind"></div>

    <footer class="contact-band">
      <p class="brand-name"><span class="brand-mark"></span>Vowsbridge-Officiants.com</p>
      <ul class="contact-list">
        <li>214 Elm Street, Brookhaven, CT 06480</li>
        <li>Marisol@Vowsbridge-Officiants.com</li>
        <li>Marisol T. Bellanova, (860) 555-0147</li>
        <li>vowsbridge-officiants.com</li>
      </ul>
    </footer>
  </main>
</body>
</html>
```